バックとタイトルにひと工夫があるとうれしいです。コピー等は入れてもらってかまいません。
添付するイラレデータCS2に全ての内容をいれます。ただし上部の大きな写真2点は本日撮り直しますので明日にでも追加でアップします。
• 高解像度JPG (.jpg)
• イラストレーター形式 (.ai)
原稿内容が一部変更になり、撮影した写真を入れておきます。はじめに添付したファイルと差し替えてください。
貼ってある写真は解像度を落としてありますので決定時に高解像度と入れ替えていただきます。
すみません。原稿1点追加になりました。

4,200円以上の宴会料理&15名様以上でいも又は麦焼酎(4合)をサービス!!
※期間 平成24年1月末日まで ※月・水・木曜日のみ

上記2行と焼酎の写真を入れてください。よろしく御願いします。

とても賑やかで、なお和のイメージが良く出ていてとても気に入りました。文字が読みづらいところが少々ありましたが訂正して頂くより自分で直した方が早いと手を加えさせていただきました。全体的なイメージはとても良かったです。

良いデザインを作成していただきありがとうございます。また依頼することがありますのでよろしくお願いします。

```html
<!DOCTYPE html>
<html lang="ja">
<head>
<meta charset="utf-8">
<title>忘新年会 ご予約承り中</title>
<link rel="stylesheet" href="https://fonts.googleapis.com/css2?family=Yuji+Boku&family=Noto+Serif+JP:wght@500;700;900&family=Noto+Sans+JP:wght@400;700;900&display=swap">
<style>
:root{
  --red:#c8161d;
  --deep-red:#8e0f14;
  --ink:#1a1a1a;
  --paper:#fbf7ee;
  --snow:#eaf2f8;
  --blue:#2a7fc0;
  --green:#3b7d2e;
  --gold:#c9a24a;
}
*{margin:0;padding:0;box-sizing:border-box}
html,body{width:849px;height:1200px;overflow:hidden;background:var(--paper)}
body{font-family:"Noto Sans JP",sans-serif;color:var(--ink);position:relative}
.flyer{position:absolute;inset:0;background:linear-gradient(180deg,#fff 0%,var(--paper) 55%,var(--snow) 100%)}
.abs{position:absolute}
.photo{position:absolute;border-radius:4px}
.intro{left:30px;top:14px;width:540px;font-size:14px;color:var(--deep-red);font-weight:700;line-height:1.5}
.offer{left:30px;display:flex;align-items:center;gap:12px}
.tag{background:var(--red);color:#fff;font-weight:900;font-size:15px;width:52px;height:46px;display:flex;align-items:center;justify-content:center;border-radius:3px}
.offer-name{font-family:"Noto Serif JP",serif;font-weight:900;font-size:30px;color:var(--red)}
.offer-price{font-family:"Noto Serif JP",serif;font-weight:900;font-size:32px;color:var(--red)}
.offer-note{font-size:11px;line-height:1.4}
.title{left:712px;top:18px;writing-mode:vertical-rl;font-family:"Yuji Boku",serif;font-size:118px;line-height:1;color:var(--ink)}
.stamp{left:612px;top:22px;width:60px;height:172px;background:var(--red);color:#fff;writing-mode:vertical-rl;font-family:"Noto Serif JP",serif;font-weight:900;font-size:25px;display:flex;align-items:center;justify-content:center;border-radius:30px}
.service{left:542px;top:200px;writing-mode:vertical-rl;font-family:"Noto Serif JP",serif;font-weight:900;font-size:22px;color:var(--red);line-height:1.25;background:rgba(255,255,255,.9);padding:6px 4px}
.service small{font-size:12px;color:var(--ink);font-weight:500}
.period{left:592px;top:528px;width:245px;font-size:11px;line-height:1.5}
.course{left:40px;top:580px;display:flex;align-items:baseline;gap:14px;line-height:1}
.course-name{font-family:"Yuji Boku",serif;font-size:58px;color:var(--blue)}
.course-price{font-family:"Noto Serif JP",serif;font-weight:900;font-size:42px;color:var(--red)}
.course-price small{font-size:16px}
.winter-band{left:0;top:654px;width:470px;height:52px;background:var(--ink);color:#fff;font-family:"Noto Serif JP",serif;font-weight:900;font-size:32px;display:flex;align-items:center;padding-left:70px}
.winter-band em{font-style:normal;color:var(--red);background:#fff;padding:0 6px;margin-right:6px;border-radius:3px}
.thanks{left:495px;top:660px;width:330px;height:28px;background:var(--red);color:#fff;font-weight:700;font-size:15px;display:flex;align-items:center;justify-content:center}
.weekday{left:530px;top:694px;font-size:13px;font-weight:700;color:var(--red)}
.lunch-name{left:495px;top:716px;font-family:"Noto Serif JP",serif;font-weight:900;font-size:26px}
.lunch-usual{left:495px;top:756px;font-size:15px;font-weight:700}
.lunch-price{left:495px;top:782px;font-family:"Noto Serif JP",serif;font-weight:900;font-size:40px;color:var(--red);line-height:1}
.lunch-price small{font-size:20px}
.ladies-box{left:495px;top:836px;width:330px;height:104px;border:2px solid var(--red);background:#fff;padding:6px 10px}
.ladies-box h3{background:var(--red);color:#fff;font-size:14px;text-align:center;margin-bottom:4px}
.ladies-box p{font-size:13px;line-height:1.5;width:225px}
.ladies-box b{color:var(--red)}
.bottom{top:952px;height:235px;background:#fff;border:2px solid var(--ink);padding:10px}
.nabe{left:20px;width:400px}
.osechi{left:430px;width:400px}
.section-label{display:inline-block;color:#fff;font-family:"Noto Serif JP",serif;font-weight:900;font-size:22px;padding:2px 14px;border-radius:3px}
.nabe .section-label{background:var(--green)}
.osechi .section-label{background:var(--red)}
.menu-list{font-size:14px;line-height:1.7;margin-top:6px}
.menu-list .price{font-weight:900;color:var(--red);font-size:18px}
</style>
</head>
<body>
<div class="flyer">
  <p class="abs intro">ひときわ華を添える季節の味わいを、心をこめたお料理でご用意いたしました。</p>

  <div class="abs offer" style="top:64px">
    <div class="tag">要予約</div>
    <span class="offer-name">宴会料理</span>
    <span class="offer-price">3,675円より</span>
  </div>
  <div class="abs offer" style="top:120px">
    <div class="tag">要予約</div>
    <span class="offer-name">飲み放題</span>
    <span class="offer-note">2名様より<br>2時間制</span>
    <span class="offer-price" style="font-size:24px">宴会料理+1,575円より</span>
  </div>

  <div class="photo" role="img" aria-label="宴会料理の盛り合わせ写真" style="left:40px;top:180px;width:490px;height:385px;background:linear-gradient(135deg,#6b4a33,#b38a5e 45%,#e7d6b8 70%,#8a5a3a)"></div>
  <div class="photo" role="img" aria-label="焼酎一升瓶の写真" style="left:596px;top:205px;width:105px;height:315px;background:linear-gradient(90deg,#1b1b1b,#4a4a4a 50%,#1b1b1b)"></div>

  <div class="abs stamp">ご予約承り中</div>
  <div class="abs title">忘新年会</div>
  <div class="abs service">いも又は麦焼酎<small>(四合)</small>をサービス!!</div>
  <p class="abs period">※期間 平成24年1月末日まで<br>※月・水・木曜日のみ</p>

  <div class="abs course">
    <span class="course-name">雪</span>
    <span class="course-price">4,200円<small>(税込)</small></span>
  </div>

  <div class="abs winter-band"><em>冬</em>の特別企画</div>
  <div class="photo" role="img" aria-label="冬の鍋料理の写真" style="left:50px;top:712px;width:420px;height:225px;background:linear-gradient(135deg,#5a3b2a,#c9935e 50%,#f2e3c6)"></div>

  <div class="abs thanks">日頃のご愛顧に感謝して</div>
  <p class="abs weekday">＊平日昼限定（土・日・祝日除く）</p>
  <p class="abs lunch-name">レディースお昼膳「綾」</p>
  <p class="abs lunch-usual">通常2,100円を</p>
  <p class="abs lunch-price"><small>税込</small>1,575円<small>に!!</small></p>

  <div class="abs ladies-box">
    <h3>冬のレディースお昼膳</h3>
    <p>松 … <b>1,575円</b>（税込）<br>竹 … <b>2,100円</b>（税込）<br>梅 … <b>2,940円</b>（税込）※ご予約優先</p>
  </div>
  <div class="photo" role="img" aria-label="お昼膳の写真" style="left:740px;top:872px;width:78px;height:60px;background:linear-gradient(135deg,#7a4b2e,#e0c49a)"></div>

  <div class="abs bottom nabe">
    <span class="section-label">鍋もの</span>
    <div class="menu-list">
      <p>・ふぐコース　・すっぽん鍋</p>
      <p>・あんこう鍋　・かに鍋</p>
      <p class="price">5,250円（税込）より</p>
      <p>・しゃぶしゃぶ　・すき焼き</p>
      <p class="price">4,200円（税込）より</p>
    </div>
    <div class="photo" role="img" aria-label="鍋料理の写真" style="left:255px;top:45px;width:130px;height:170px;background:linear-gradient(135deg,#6a3a22,#d49a62)"></div>
  </div>

  <div class="abs bottom osechi">
    <span class="section-label">おせち料理</span>
    <div class="menu-list">
      <p>お重 三段</p>
      <p class="price">21,000円（税込）</p>
      <p>お重 二段</p>
      <p class="price">15,750円（税込）</p>
      <p style="font-size:12px">※12月20日までにご予約ください</p>
    </div>
    <div class="photo" role="img" aria-label="おせち重箱の写真" style="left:220px;top:45px;width:165px;height:170px;background:linear-gradient(135deg,#2a1a14,#9c2a1e 45%,var(--gold))"></div>
  </div>
</div>
</body>
</html>
```